New Website for World Wide Charity (VELORA)

We need a dynamic web design for our brand new charity organisation that will be working worldwide. We will be funded by donations so need to attract people to donate.

What We Do
We work to optimise the wellbeing of the planet, the animals and all that live within. Our slogan is Achieving Vibrational Equilibrium.

We have included a Powerpoint document which may help you understand what we need, it is just an idea for structure and style, it is not set in stone so feel free to be as creative as you like!
Updates

Designs look the same

Target Market(s)

Adults 18+ with an interest in animal, environmental. Businesses that may like to support our natural world or already support our natural world.

Number of Pages Required

3 page

Colors

Designer to choose colors to be used in the design.

Requirements
Must have
• We need the website to be easy to use and understand.

Web pages will be Home, What We Do, Who We Are, Success Stories, What You Can Do (Blog section), Seek Help, Donate, Join.
Nice to have
• Natural feel, easy to navigate, Ideally the website will look natural and organic.

Natural colours, blues, greens, sand, gold, brown, grey, silver, Orange and yellow for impact.
Should not have
• Should not have a dark coloured theme.

```html
<!DOCTYPE html>
<html lang="en">
<head>
<meta charset="utf-8">
<title>VELORA – Help Raise World Vibration</title>
<link rel="stylesheet" href="https://fonts.googleapis.com/css2?family=Montserrat:wght@500;600;700;800&family=Open+Sans:wght@400;600&display=swap">
<style>
:root{
  --forest-deep:#173d31;
  --forest:#2a5a49;
  --lake:#3f6f7a;
  --sky-blue:#2f5b98;
  --deep-blue:#23478a;
  --night-blue:#1b3a74;
  --accent-blue:#2f63b3;
  --orange:#ea921d;
  --leaf:#4aa04a;
  --white:#ffffff;
  --card:#eef1f4;
  --ink:#2d3c55;
}
*{box-sizing:border-box;margin:0;padding:0}
html,body{width:1200px;height:3564px;overflow:hidden}
body{position:relative;font-family:"Open Sans",Arial,sans-serif;color:var(--white);background:var(--deep-blue)}
.backdrop{position:absolute;inset:0;background:linear-gradient(180deg,#e9eef0 0px,#7f9d93 70px,var(--forest) 150px,var(--forest-deep) 500px,#21503f 900px,#2f5f5a 1400px,var(--lake) 1750px,var(--sky-blue) 2000px,#2c559a 2500px,#3a68a8 2850px,var(--deep-blue) 3100px)}
.abs{position:absolute}
/* header */
.brand{left:148px;top:24px;display:flex;align-items:center;gap:10px}
.brand-mark{width:58px;height:58px;border-radius:50%;background:var(--white);border:3px solid #cfd8de}
.brand-name{font-family:"Montserrat",sans-serif;font-weight:700;font-size:15px;color:var(--ink);letter-spacing:1px}
.main-nav{left:358px;top:46px;display:flex;gap:42px;font-family:"Montserrat",sans-serif;font-size:13px;font-weight:500}
.main-nav a{color:#3a5f9a;text-decoration:none}
.main-nav a.current{color:var(--leaf);font-weight:600}
/* hero */
.hero{left:0;top:160px;width:1200px;text-align:center}
.hero h1{font-family:"Montserrat",sans-serif;font-weight:800;font-size:35px;letter-spacing:1px}
.hero p{width:560px;margin:22px auto 0;font-size:14px;line-height:21px}
.btn{display:inline-block;background:var(--deep-blue);color:var(--white);font-family:"Montserrat",sans-serif;font-size:10px;font-weight:600;letter-spacing:.5px;padding:9px 20px;text-decoration:none}
.hero .btn{margin-top:48px;padding:11px 30px}
/* cards */
.card{text-align:center;padding:72px 16px 0;background:var(--card)}
.card h2{font-family:"Montserrat",sans-serif;font-weight:700;font-size:20px;color:var(--accent-blue);letter-spacing:.5px}
.card p{font-size:11px;line-height:15px;color:#4a5568;margin:12px 0 18px}
.card .btn{font-size:9px;padding:7px 24px}
.card--env{left:150px;top:700px;width:178px;height:232px}
.card--animal{left:460px;top:688px;width:212px;height:258px;background:var(--orange)}
.card--animal h2,.card--animal p{color:var(--white)}
.card--human{left:795px;top:700px;width:172px;height:232px}
/* stories */
.story h2{font-family:"Montserrat",sans-serif;font-weight:700;font-size:24px;letter-spacing:1px;margin-bottom:20px}
.story p{font-size:13px;line-height:20px;margin-bottom:20px}
.story--env{left:645px;top:1340px;width:420px}
.story--animal{left:145px;top:1950px;width:400px}
.story--human{left:645px;top:2635px;width:400px}
.photo{display:block}
/* footer */
.footer-rule{left:150px;top:3130px;width:910px;height:2px;background:rgba(255,255,255,.7)}
.footer-brand{left:150px;top:3180px;width:200px;text-align:center}
.footer-brand .brand-mark{margin:0 auto 12px;width:70px;height:70px}
.footer-brand p{font-size:11px;line-height:16px}
.footer-col{top:3180px;font-family:"Montserrat",sans-serif}
.footer-col h3{font-size:12px;font-weight:700;margin-bottom:36px;letter-spacing:.5px}
.footer-col li{list-style:none;font-size:11px;font-weight:500;margin-bottom:14px}
.col-involved{left:440px}.col-help{left:640px}.col-legal{left:825px}
.bottom-bar{left:0;top:3526px;width:1200px;height:38px;background:var(--night-blue);display:flex;align-items:center;justify-content:space-between;padding:0 150px;font-size:12px}
.socials{display:flex;gap:8px}
.socials span{width:20px;height:20px;border-radius:50%;background:var(--white);opacity:.9}
</style>
</head>
<body>
<div class="backdrop" role="img" aria-label="Misty pine forest and lake landscape fading into a blue mountain sky"></div>

<header>
  <div class="abs brand"><span class="brand-mark"></span><span class="brand-name">VELORA</span></div>
  <nav class="abs main-nav">
    <a class="current" href="#">Home</a><a href="#">What We Do</a><a href="#">Who We Are</a><a href="#">Success Stories</a><a href="#">What You Can Do</a><a href="#">Donate and Join</a>
  </nav>
</header>

<section class="abs hero">
  <h1>HELP RAISE WORLD VIBRATION</h1>
  <p>We connect people, places and purpose to restore balance across the planet. Every gift helps protect wild land, care for animals and support communities finding their way back to harmony.</p>
  <a class="btn" href="#">MAKE A DIFFERENCE</a>
</section>

<article class="abs card card--env"><h2>ENVIRONMENT</h2><p>Restoring forests, rivers and soil so the living planet can breathe again.</p><a class="btn" href="#">FIND OUT MORE</a></article>
<article class="abs card card--animal"><h2>ANIMAL</h2><p>Rescue, shelter and care for creatures wild and domestic around the world.</p><a class="btn" href="#">FIND OUT MORE</a></article>
<article class="abs card card--human"><h2>HUMAN</h2><p>Support for people and communities seeking balance, health and hope.</p><a class="btn" href="#">FIND OUT MORE</a></article>

<svg class="abs photo" style="left:140px;top:1350px" width="310" height="360" viewBox="0 0 310 360" role="img" aria-label="Photo of a small leafy tree in a pot">
  <path d="M40 60 C90 5 230 0 280 60 C320 120 300 250 250 310 C200 360 90 350 45 300 C5 250 0 120 40 60Z" fill="#2d3a2a" stroke="#2f63b3" stroke-width="10"/>
</svg>
<section class="abs story story--env">
  <h2>ENVIRONMENT</h2>
  <p>Healthy land and water are the ground of every life. We plant native trees, clean rivers and protect fragile habitats with local partners who know their land best. Our teams measure results carefully so each donation turns into lasting, visible change on the ground.</p>
  <p>In the months ahead we will restore wetlands, seed meadows for pollinators and help villages manage forests they depend on. Volunteers can join planting days, and businesses can sponsor whole hectares of recovering land while tracking progress online.</p>
</section>

<section class="abs story story--animal">
  <h2>ANIMAL</h2>
  <p>Every creature deserves safety and care. We fund rescue centres, veterinary teams and sanctuaries for animals harmed by loss of habitat, neglect or trade. Our partners return healthy animals to the wild wherever they can thrive again.</p>
  <p>For pets without a home we support shelters that rehome, feed and heal. Your gift buys food, medicine and time, giving each animal a real chance at a calm and loving life.</p>
</section>
<svg class="abs photo" style="left:755px;top:1895px" width="350" height="340" viewBox="0 0 350 340" role="img" aria-label="Photo of two golden puppies sitting in a flower meadow">
  <path d="M60 40 C120 0 270 10 320 70 C355 130 340 250 280 300 C220 345 90 335 40 280 C0 230 5 90 60 40Z" fill="#c99a52" stroke="#ea921d" stroke-width="10"/>
</svg>

<svg class="abs photo" style="left:155px;top:2595px" width="360" height="390" viewBox="0 0 360 390" role="img" aria-label="Photo of a smiling man in a cap and sunglasses with his dog">
  <path d="M50 70 C110 5 270 0 320 60 C360 120 350 280 300 340 C240 395 100 385 50 330 C5 275 0 135 50 70Z" fill="#6f7f8c" stroke="#ffffff" stroke-width="8"/>
</svg>
<section class="abs story story--human">
  <h2>HUMAN</h2>
  <p>People flourish when they feel connected to nature and to each other. We run outdoor wellbeing programmes, community gardens and quiet retreats for those facing stress, loss or isolation, open to every age and background.</p>
  <p>Anyone can ask for help through our Seek Help page. Trained volunteers listen first, then guide each person toward local support, shared activity and a steadier sense of balance.</p>
</section>

<footer>
  <div class="abs footer-rule"></div>
  <div class="abs footer-brand">
    <div class="brand-mark"></div>
    <p>Achieving vibrational equilibrium for the planet, its animals and all who live within it.</p>
  </div>
  <div class="abs footer-col col-involved"><h3>GET INVOLVED</h3><ul><li>JOIN US</li><li>FUNDRAISE</li><li>DONATE</li><li>SHOP</li></ul></div>
  <div class="abs footer-col col-help"><h3>GET HELP</h3><ul><li>CONTACT US</li><li>MEDIA</li></ul></div>
  <div class="abs footer-col col-legal"><h3>LEGAL</h3><ul><li>TERMS AND CONDITIONS</li><li>COOKIES</li><li>PRIVACY POLICY</li></ul></div>
  <div class="abs bottom-bar"><span>© All Rights are Reserved</span><div class="socials"><span></span><span></span><span></span></div></div>
</footer>
</body>
</html>
```